New CD - "Tunes About Marla" (Jazz piano standards)

We need a CD design for album of jazz piano standards. The music is elegant, fun, and artistic. Appeals to all lovers of Halvorsen, Brenton, Dubrow, etc. Includes Red Harbor, Can't Stop Dancin', Harbor Serenade, She Keeps A Secret In Her Pocket, Rain Falls On Quiet Streets, Lazy Tuesday, (Tonight) Across The Meadow, Hours by Candle and Lace, When Rivers Bend, Only If You Call, Your Quiet Spark, She Always Left The Door, Remarkable Dawn, Prelude Op. 28, No. 15 "Lamplight"/T. Varga.

Target Market(s)

Anyone who likes piano music.

```html
<!DOCTYPE html>
<html lang="en">
<head>
<meta charset="utf-8">
<title>Tunes About Marla – CD Design</title>
<link rel="stylesheet" href="https://fonts.googleapis.com/css2?family=Michroma&family=Cinzel:wght@400&family=Oswald:wght@300;400&family=Source+Sans+3:wght@400&display=swap">
<style>
  :root {
    --paper: #ffffff;
    --ink: #111111;
    --night-top: #16275a;
    --night-mid: #2d4c9c;
    --night-water: #0c1a47;
    --night-low: #1d3880;
    --gold: #e9c23a;
    --white: #ffffff;
    --tray-grey: #a9b2ac;
    --tray-edge: #8b918d;
    --portrait-light: #d8d6cc;
    --portrait-dark: #5a4a3c;
  }
  html, body {
    margin: 0;
    padding: 0;
    width: 1200px;
    height: 1200px;
    overflow: hidden;
    background: var(--paper);
  }
  .sheet { display: block; width: 1200px; height: 1200px; }
  .panel-label { font-family: "Michroma", sans-serif; font-size: 31px; fill: var(--ink); letter-spacing: 1px; }
  .series-name { font-family: "Source Sans 3", sans-serif; fill: var(--white); letter-spacing: 1px; }
  .artist-name { font-family: "Oswald", sans-serif; font-weight: 300; fill: var(--white); }
  .album-title { font-family: "Cinzel", serif; fill: var(--gold); letter-spacing: 1px; }
  .spine-title { font-family: "Cinzel", serif; fill: var(--gold); font-size: 17px; letter-spacing: 1px; }
  .spine-artist { font-family: "Oswald", sans-serif; font-weight: 300; fill: var(--white); font-size: 15px; }
  .track { font-family: "Source Sans 3", sans-serif; font-size: 13px; fill: var(--white); }
  .fine-print { font-family: "Source Sans 3", sans-serif; fill: var(--white); }
</style>
</head>
<body>
<svg class="sheet" viewBox="0 0 1200 1200" xmlns="http://www.w3.org/2000/svg">
  <defs>
    <linearGradient id="night-sky" x1="0" y1="0" x2="0" y2="1">
      <stop offset="0" stop-color="var(--night-top)"/>
      <stop offset="0.45" stop-color="var(--night-mid)"/>
      <stop offset="0.6" stop-color="var(--night-water)"/>
      <stop offset="1" stop-color="var(--night-low)"/>
    </linearGradient>
    <linearGradient id="portrait-tone" x1="0" y1="0" x2="1" y2="1">
      <stop offset="0" stop-color="var(--tray-grey)"/>
      <stop offset="0.5" stop-color="var(--portrait-light)"/>
      <stop offset="1" stop-color="var(--portrait-dark)"/>
    </linearGradient>
    <clipPath id="disc-clip"><circle cx="297" cy="922" r="240"/></clipPath>
  </defs>

  <!-- Panel labels -->
  <text class="panel-label" x="84" y="124">CD TRAY</text>
  <text class="panel-label" x="84" y="166">- BACK</text>
  <text class="panel-label" x="48" y="655">CD</text>

  <!-- Tray back -->
  <g class="tray-back">
    <rect x="352" y="17" width="832" height="653" fill="url(#night-sky)" role="img" aria-label="Night city skyline reflected in water"/>
    <text class="series-name" x="770" y="82" font-size="17" text-anchor="middle">JAZZ PIANO STANDARDS</text>
    <text class="artist-name" x="768" y="170" font-size="26" text-anchor="middle">Gregory Ashford</text>
    <text class="album-title" x="770" y="213" font-size="22" text-anchor="middle">Tunes About Marla</text>

    <text class="spine-title" transform="translate(376 262) rotate(-90)">Tunes About Marla</text>
    <text class="spine-artist" transform="translate(376 575) rotate(-90)">Gregory Ashford</text>
    <text class="spine-artist" transform="translate(1159 100) rotate(90)">Gregory Ashford</text>
    <text class="spine-title" transform="translate(1159 450) rotate(90)">Tunes About Marla</text>

    <g class="tracklist">
      <text class="track" x="611" y="249">1.&#160; She Keeps A Secret In Her Pocket /H. Morrow&#160; (2:22)</text>
      <text class="track" x="611" y="273">2.&#160; Rain Falls On Quiet Streets /J. Pell &amp; O. Lindqvist&#160; (3:29)</text>
      <text class="track" x="611" y="296">3.&#160; Red Harbor /R. Brenton&#160; (3:31)</text>
      <text class="track" x="611" y="320">4.&#160; Lazy Tuesday /H. Morrow&#160; (2:08)</text>
      <text class="track" x="611" y="343">5.&#160; Across The Meadow /H. Morrow &amp; E.Y. Tillman&#160; (4:12)</text>
      <text class="track" x="611" y="367">6.&#160; Hours by Candle and Lace /H. Dubrow &amp; J. Ferris&#160; (2:54)</text>
      <text class="track" x="611" y="390">7.&#160; When Rivers Bend /H. Kessler&#160; (1:51)</text>
      <text class="track" x="611" y="414">8.&#160; Can't Stop Dancin' /F. Walden&#160; (2:15)</text>
      <text class="track" x="611" y="437">9.&#160; Only If You Call /G. Halvorsen&#160; (4:17)</text>
      <text class="track" x="607" y="461">10.&#160; Harbor Serenade /K. Dunmore &amp; J. Petrak&#160; (2:21)</text>
      <text class="track" x="607" y="484">11.&#160; Your Quiet Spark /V. Hale&#160; (3:34)</text>
      <text class="track" x="607" y="508">12.&#160; She Always Left The Door /R. Brenton&#160; (2:49)</text>
      <text class="track" x="607" y="531">13.&#160; Remarkable Dawn /G. Halvorsen&#160; (2:13)</text>
      <text class="track" x="607" y="555">14.&#160; Prelude Op. 28, No. 15 "Lamplight" /T. Varga&#160; (5:46)</text>
    </g>
    <text class="fine-print" x="628" y="647" font-size="12">Copyright © 2012 Gregory Ashford:&#160; All Rights Reserved</text>
  </g>

  <!-- Disc -->
  <g class="disc">
    <g clip-path="url(#disc-clip)">
      <rect x="57" y="682" width="480" height="480" fill="url(#night-sky)" role="img" aria-label="Night city skyline reflected in water"/>
    </g>
    <circle cx="297" cy="922" r="18" fill="var(--paper)"/>
    <text class="series-name" x="297" y="755" font-size="15" text-anchor="middle">JAZZ PIANO STANDARDS</text>
    <text class="album-title" x="297" y="845" font-size="16" text-anchor="middle">Tunes About Marla</text>
    <text class="artist-name" font-size="20" transform="translate(290 1000) rotate(90)">Gregory Ashford</text>
    <rect x="446" y="960" width="60" height="35" fill="var(--white)"/>
    <text class="fine-print" font-size="6" transform="translate(226 1141) rotate(5)">Copyright © 2012 Gregory Ashford&#160;&#160; All Rights Reserved</text>
  </g>

  <!-- Tray inside -->
  <g class="tray-inside">
    <rect x="578" y="694" width="605" height="476" fill="var(--tray-grey)"/>
    <rect x="578" y="694" width="32" height="476" fill="var(--tray-edge)"/>
    <rect x="1151" y="694" width="32" height="476" fill="var(--tray-edge)"/>
    <rect x="700" y="800" width="451" height="370" fill="url(#portrait-tone)" role="img" aria-label="Portrait of the pianist in a dark suit"/>
    <text class="panel-label" x="620" y="757">CD TRAY- INSIDE</text>
  </g>
</svg>
</body>
</html>
```